依頼概要
■依頼の目的/概要
弊社が販売を予定しているオリジナルサイダーのラベルデザインをお願いします。
■依頼詳細
今回は弊社が販売する吟醸香がするオリジナルサイダーラベルのデザインをお願いします。
商品名は雲雀野サイダーです。

■その他要望
イメージは昭和レトロなサイダー感で、それでいて店頭で目に付くデザイン。
仕込み水を使用したサイダーなのでその表記も入れる。
商品名は雲雀野サイダーです。
添付資料は弊社のロゴです、使っても使わなくてもどちらでも結構です。

その他何かご不明な点がございましたら、お気軽にご質問下さい。
よろしくお願いいたします。

```html
<!DOCTYPE html>
<html lang="ja">
<head>
<meta charset="UTF-8">
<title>雲雀野サイダー ラベル</title>
<link href="https://fonts.googleapis.com/css2?family=Zen+Maru+Gothic:wght@500;700;900&family=Noto+Sans+JP:wght@400;500&display=swap" rel="stylesheet">
<style>
  :root {
    --teal: #8fd0cb;
    --orange: #ef8a5e;
    --paper: #ffffff;
    --ink: #4a4a4a;
    --emblem: #ffffff;
  }
  * { margin: 0; padding: 0; box-sizing: border-box; }
  html, body {
    width: 854px;
    height: 1200px;
    overflow: hidden;
    background: var(--paper);
  }
  .sheet {
    position: relative;
    width: 854px;
    height: 1200px;
  }
  .label {
    position: absolute;
    left: 149px;
    width: 556px;
    height: 556px;
    border-radius: 50%;
    text-align: center;
  }
  .label--teal { top: 28px; background: var(--teal); --accent: var(--orange); }
  .label--orange { top: 614px; background: var(--orange); --accent: var(--teal); }

  .label__tagline {
    position: absolute;
    top: 52px;
    left: 0; right: 0;
    font-family: "Noto Sans JP", sans-serif;
    font-weight: 500;
    font-size: 16px;
    color: var(--ink);
    letter-spacing: 0.04em;
  }
  .label__name {
    position: absolute;
    top: 72px;
    left: 0; right: 0;
    font-family: "Zen Maru Gothic", sans-serif;
    font-weight: 900;
    font-size: 84px;
    line-height: 1;
    color: var(--accent);
    letter-spacing: 0.06em;
  }
  .label__romaji {
    position: absolute;
    top: 166px;
    left: 0; right: 0;
    font-family: "Noto Sans JP", sans-serif;
    font-size: 12px;
    color: var(--ink);
    letter-spacing: 0.12em;
  }
  .label__emblem {
    position: absolute;
    top: 196px;
    left: 50%;
    width: 164px;
    height: 164px;
    margin-left: -82px;
    border-radius: 50%;
    background: var(--emblem);
  }
  .label__product {
    position: absolute;
    top: 372px;
    left: 0; right: 0;
    font-family: "Zen Maru Gothic", sans-serif;
    font-weight: 900;
    font-size: 96px;
    line-height: 1;
    color: var(--accent);
    letter-spacing: 0.04em;
  }
  .label__en {
    position: absolute;
    top: 490px;
    left: 0; right: 0;
    font-family: "Noto Sans JP", sans-serif;
    font-size: 12px;
    color: var(--ink);
    letter-spacing: 0.12em;
  }
</style>
</head>
<body>
  <main class="sheet">
    <section class="label label--teal">
      <p class="label__tagline">仕込み水を使用したサイダー</p>
      <h1 class="label__name">雲雀野</h1>
      <p class="label__romaji">HIBARINO</p>
      <div class="label__emblem" role="img" aria-label="魚と盃の紋章イラスト"></div>
      <p class="label__product">サイダー</p>
      <p class="label__en">CIDER</p>
    </section>

    <section class="label label--orange">
      <p class="label__tagline">仕込み水を使用したサイダー</p>
      <h2 class="label__name">雲雀野</h2>
      <p class="label__romaji">HIBARINO</p>
      <div class="label__emblem" role="img" aria-label="魚と盃の紋章イラスト"></div>
      <p class="label__product">サイダー</p>
      <p class="label__en">CIDER</p>
    </section>
  </main>
</body>
</html>
```